Need an ebook cover for a memoir about growing up in NYC in the 90s and getting in lots of trouble.

Harbor Lane Rebel is the true story of an over-privileged hoodlum
growing up in Manhattan in the 90s during the golden era of hip-hop. The book follows the troubled youth all the way from hanging off the back of subway cars at fourteen, through a romance with a mafia princess doomed for disaster, to a law school class where the unreformed miscreant sits politely with his hand raised. The cover should feature a white teenager, perhaps in a puffy Ridgeline Coat jacket, in NYC -- or whatever you feel; I am open. I've attached a sample of the memoir for your reference. I've also attached a sample of what I think the title should look like: Harbor Lane Rebel; Marlow Quint; A Memoir.

The name of the author is Marlow Quint. It is not Tobin Fairley.

```html
<!DOCTYPE html>
<html lang="en">
<head>
<meta charset="utf-8">
<title>Harbor Lane Rebel — A Memoir by Marlow Quint</title>
<link href="https://fonts.googleapis.com/css2?family=Bebas+Neue&display=swap" rel="stylesheet">
<style>
  :root {
    --page-bg: #f6f3f3;
    --cover-white: #ffffff;
    --title-red: #ee0a23;
    --ink-black: #0c0c0c;
    --photo-light: #d8cbc5;
    --photo-mid: #b9aca7;
    --photo-dark: #1a1718;
  }
  * { margin: 0; padding: 0; box-sizing: border-box; }
  html, body {
    width: 1200px;
    height: 1000px;
    overflow: hidden;
    background: var(--page-bg);
  }
  .canvas {
    position: relative;
    width: 1200px;
    height: 1000px;
  }
  .cover {
    position: absolute;
    left: 255px;
    top: 40px;
    width: 690px;
    height: 920px;
    background: var(--cover-white);
    overflow: hidden;
    font-family: "Bebas Neue", "Oswald", sans-serif;
    text-align: center;
    box-shadow: 0 6px 24px rgba(0,0,0,0.08);
  }
  .cover-title-line,
  .cover-byline,
  .cover-author {
    position: absolute;
    left: 0;
    width: 100%;
    line-height: 1;
    white-space: nowrap;
  }
  .cover-title-line { color: var(--title-red); }
  .cover-title-line--first { top: 17px; font-size: 145px; }
  .cover-title-line--second { top: 133px; font-size: 180px; }
  .cover-byline {
    top: 321px;
    font-size: 50px;
    color: var(--ink-black);
  }
  .cover-author {
    top: 361px;
    font-size: 90px;
    color: var(--ink-black);
  }
  .cover-photo {
    position: absolute;
    left: 0;
    top: 460px;
    width: 690px;
    height: 460px;
    background:
      linear-gradient(100deg, var(--photo-dark) 0%, #3a3334 22%, var(--photo-mid) 42%, var(--photo-light) 60%, var(--photo-light) 100%);
  }
</style>
</head>
<body>
  <main class="canvas">
    <article class="cover">
      <h1 class="cover-title">
        <span class="cover-title-line cover-title-line--first">Harbor Lane</span>
        <span class="cover-title-line cover-title-line--second">Rebel</span>
      </h1>
      <p class="cover-byline">A Memoir By</p>
      <p class="cover-author">Marlow Quint</p>
      <div class="cover-photo" role="img" aria-label="High-contrast black and white photo of a teenage boy in a dark hooded jacket, head bowed, against a textured pale wall"></div>
    </article>
  </main>
</body>
</html>
```